Biz card for my counselling/social work practice

Biz card design for my counselling practice, focus on well-being, I am a social worker who also teaches meditation and workshops but my main focus for the card is my counselling practice. My website reveals a gentle flowing quality which I would life reflected in my card. This business card will be designed to share with other practitioners who are looking for support with their clients to take their healing to another level or well-being.

Target Market(s)

professionals seeking mental health counselling/men/women/ those seeking to improve their well-being through insight based counselling to optimize their lives and process trauma or limiting patterns

Industry/Entity Type

Counsellor

Contact Information for Business Card

Info on the card: perhaps text is aligned left?
Marla Finch, MSW, RSW
Counsellor
250.555.0142
info@marlafinch.ca
www.marlafinch.ca

Please use a modern font doesn’t need to be the one chosen below. Thank you

Font styles to use
Serif

Colors
3176b5
33a6d7
33b8a4
6b449b
abd037
d2a4cc
e55fa2

Requirements
Must have
• My business card details on front
• Backside
• Accelerated Resolution Therapy
• Cognitive Behavioral Therapy
• Mindfulness Informed Therapy
Nice to have
• I would like the card to be basic, (white or creme without too much bold colour) and with perhaps a stripe or band of vertical colour in blue or green (or a merge of colour) perhaps embossed or in a negative space. (this is one idea, but do not want the card to be too feminine or interest only women as i see men too so this is only an idea, but not 100 percent on this.
• I do not have a logo. I would prefer to heart from my website not to be used in the design as i am considering modifying this and re-branding.
Should not have
• too bold colours or bright yellow/blacks. i Like tones that are greens, blues.

```html
<!DOCTYPE html>
<html lang="en">
<head>
<meta charset="utf-8">
<title>Marla Finch — Business Card</title>
<link rel="stylesheet" href="https://fonts.googleapis.com/css2?family=Open+Sans:wght@400&family=Source+Serif+4:opsz,wght@8..60,300;8..60,400&display=swap">
<style>
  :root {
    --page-bg: #f5f5f5;
    --card-bg: #ffffff;
    --label-ink: #1e1e1e;
    --name-ink: #6e6e6e;
    --role-ink: #3176b5;
    --detail-ink: #7a7a7a;
    --mono-green: #dcefea;
    --mono-blue: #d9e6f3;
  }
  * { margin: 0; padding: 0; box-sizing: border-box; }
  html, body {
    width: 899px;
    height: 1200px;
    overflow: hidden;
    background: var(--page-bg);
  }
  .sheet {
    position: relative;
    width: 899px;
    height: 1200px;
  }
  .side-label {
    position: absolute;
    left: 0;
    width: 899px;
    text-align: center;
    font-family: "Open Sans", sans-serif;
    font-size: 35px;
    font-weight: 400;
    color: var(--label-ink);
    letter-spacing: -0.5px;
  }
  .side-label--front { top: 50px; left: 3px; }
  .side-label--back { top: 636px; left: -14px; }

  .card {
    position: absolute;
    width: 766px;
    height: 449px;
    background: var(--card-bg);
    overflow: hidden;
    font-family: "Source Serif 4", serif;
  }
  .card--front { left: 67px; top: 120px; }
  .card--back { left: 63px; top: 698px; }

  .monogram-field {
    position: absolute;
    top: 0;
    right: 0;
    width: 305px;
    height: 100%;
    background:
      linear-gradient(90deg, var(--card-bg) 0%, rgba(255,255,255,0) 35%),
      linear-gradient(180deg, var(--mono-green) 0%, var(--mono-green) 42%, var(--mono-blue) 62%, var(--mono-blue) 100%);
  }

  .identity {
    position: absolute;
    left: 60px;
    top: 128px;
  }
  .identity__name {
    font-size: 31px;
    font-weight: 400;
    color: var(--name-ink);
    line-height: 37px;
  }
  .identity__role {
    font-size: 27px;
    font-weight: 400;
    color: var(--role-ink);
    line-height: 37px;
  }
  .contact {
    position: absolute;
    left: 60px;
    top: 249px;
    list-style: none;
    font-size: 23px;
    font-weight: 300;
    color: var(--detail-ink);
    line-height: 35px;
  }

  .services {
    position: absolute;
    left: 60px;
    top: 158px;
    list-style: none;
    font-size: 25px;
    font-weight: 300;
    color: var(--detail-ink);
    line-height: 44px;
  }
  .services li::before {
    content: "•";
    font-size: 16px;
    margin-right: 6px;
    vertical-align: 3px;
  }
</style>
</head>
<body>
<main class="sheet">
  <h2 class="side-label side-label--front">FRONT</h2>
  <section class="card card--front">
    <div class="monogram-field" role="img" aria-label="Large faint calligraphic monogram in soft green and blue"></div>
    <div class="identity">
      <h1 class="identity__name">Marla Finch, MSW, RSW</h1>
      <p class="identity__role">Counsellor</p>
    </div>
    <ul class="contact">
      <li>250.555.0142</li>
      <li>info@marlafinch.ca</li>
      <li>www.marlafinch.ca</li>
    </ul>
  </section>

  <h2 class="side-label side-label--back">BACK</h2>
  <section class="card card--back">
    <div class="monogram-field" role="img" aria-label="Large faint calligraphic monogram in soft green and blue"></div>
    <ul class="services">
      <li>Accelerated Resolution Therapy</li>
      <li>Cognitive Behavioral Therapy</li>
      <li>Mindfulness Informed Therapy</li>
    </ul>
  </section>
</main>
</body>
</html>
```